Brighter Than Dawn Home Entertainment

We are a home theater installation company focus on front projection system and home theater surround system. We built highend home theater for people to enjoy movie, sports and gaming on big screen at home.
I'm looking for a dispaly to showcase our work as well as help people build their home theater

Number of Pages Required

3 page

Colors

Designer to choose colors to be used in the design.

Requirements
Must have
• Home Page
• What we do
• Who we are
• Gallery
• Contact Us
Nice to have
• Picture jump out of big screen make a 3D feeling

```html
<!DOCTYPE html>
<html lang="en">
<head>
<meta charset="utf-8">
<title>Brighter Than Dawn Home Entertainment</title>
<link href="https://fonts.googleapis.com/css2?family=Lato:ital,wght@0,300;0,400;0,700;1,300;1,400&display=swap" rel="stylesheet">
<style>
:root{
  --purple:#8d5cb6;
  --purple-dark:#7a4aa3;
  --teal:#3cc7a5;
  --ink:#23272f;
  --ink-deep:#1c1f26;
  --paper:#eef0f3;
  --white:#ffffff;
  --grey:#8a8f99;
  --text:#3d4148;
}
*{margin:0;padding:0;box-sizing:border-box}
html,body{width:1200px;height:4273px;overflow:hidden}
body{font-family:"Lato",sans-serif;color:var(--text);background:var(--white);position:relative}
section,footer{position:absolute;left:0;width:1200px;overflow:hidden}
.abs{position:absolute}
.media{position:absolute}
.btn{position:absolute;display:flex;align-items:center;justify-content:center;height:34px;border-radius:17px;background:var(--teal);color:var(--white);font-size:12px;box-shadow:0 8px 16px rgba(0,0,0,.25)}

/* hero */
.hero{top:0;height:633px;background:linear-gradient(90deg,#2a3442 0%,#0e1117 45%,#161a21 100%)}
.brand{left:28px;top:20px;color:var(--purple);font-size:40px;font-weight:700;letter-spacing:1px}
.search{left:822px;top:40px;width:192px;height:34px;border-radius:17px;background:#2c313a;color:#9aa0aa;font-size:12px;padding:0 16px;display:flex;align-items:center;justify-content:space-between}
.call{left:1028px;top:40px;width:88px;height:34px;border-radius:17px;background:var(--purple);color:var(--white);font-size:12px;font-weight:700;display:flex;align-items:center;justify-content:center}
.menu{left:1044px;top:92px;width:56px;height:44px;border:1px solid #555b66}
.hero h1{left:478px;top:288px;font-weight:300;font-size:52px;line-height:64px;color:var(--white);white-space:nowrap}
.hero .lead{left:480px;top:432px;width:440px;color:#d8dce2;font-size:13px;line-height:21px}

/* what we do */
.what{top:633px;height:387px;background:var(--purple)}
.what h2{left:156px;top:94px;font-weight:300;font-size:30px;color:var(--white)}
.what p{left:156px;top:142px;width:420px;color:#efe6f7;font-size:13px;line-height:20px}

/* features */
.features{top:1020px;height:391px;background:var(--paper)}
.feature{position:absolute;top:64px;width:270px;height:300px}
.feature h3{font-weight:300;font-size:25px;color:#4a4f57;margin-bottom:14px}
.feature .sub{color:var(--grey);font-size:15px;line-height:22px;margin-bottom:18px;font-weight:300}
.feature .body{color:#777c86;font-size:11px;line-height:18px}
.feature .btn{top:240px;left:12px;width:112px}

/* who we are */
.who{top:1411px;height:470px;background:var(--ink)}
.who h2{left:0;width:1200px;top:86px;text-align:center;font-weight:300;font-size:34px;color:var(--white)}
.who p{left:156px;top:145px;width:888px;text-align:center;color:#a5aab3;font-size:13px;line-height:22px}

/* values */
.values{top:1881px;height:399px;background:var(--ink-deep)}
.value{position:absolute;top:70px;width:200px}
.value h4{color:var(--white);font-weight:400;font-size:16px;margin:18px 0 10px}
.value p{color:#9096a0;font-size:11px;line-height:18px}

/* gallery */
.gallery{top:2280px;height:428px;background:var(--paper)}
.gallery h2{left:186px;top:70px;font-weight:300;font-size:32px;color:#4a4f57}
.gallery .sub{left:156px;top:124px;width:380px;color:var(--grey);font-size:15px;line-height:22px;font-weight:300}
.gallery .body{left:156px;top:224px;width:390px;color:#5b6068;font-size:12px;line-height:20px}

/* stories */
.stories{top:2708px;height:570px;background:var(--white)}
.quote-card{left:585px;top:0;width:615px;height:342px;background:var(--purple);padding:54px 42px;color:var(--white)}
.quote-card .date{font-size:11px;opacity:.8;margin-bottom:10px}
.quote-card blockquote{font-style:italic;font-weight:300;font-size:23px;line-height:31px;white-space:nowrap}
.author{display:flex;align-items:center;gap:14px;margin-top:26px;font-size:12px}
.avatar{width:40px;height:40px;border-radius:50%;background:#c9c3cf}
.post{left:148px;top:342px;width:437px;height:228px;background:var(--white);padding:26px 30px}
.post h3{font-size:18px;font-weight:400;color:#222;line-height:24px;margin-bottom:14px}
.post p{font-size:11px;line-height:17px;color:#999}
.tag{left:585px;top:326px;background:#1e1f24;color:#fff;font-size:9px;padding:4px 10px}

/* project */
.project{top:3278px;height:570px;background:#d9d6d3}
.project .panel{left:0;top:0;width:580px;height:342px;background:var(--purple);padding:28px 0 0 151px}
.project h2{color:var(--white);font-size:28px;font-weight:700;margin-bottom:10px}
.project blockquote{color:var(--white);font-style:italic;font-weight:300;font-size:24px;line-height:33px;white-space:nowrap}

/* footer */
.footer{top:3848px;height:425px;background:var(--ink)}
.footer h2{left:156px;top:26px;color:var(--white);font-size:19px;font-weight:400}
.footer .intro{left:156px;top:60px;width:500px;color:#aeb3bb;font-size:11px;line-height:17px}
.links{position:absolute;top:199px;width:140px;color:#cfd3d9;font-size:11px;line-height:18px}
.links h5{color:var(--white);font-size:12px;font-weight:700;margin-bottom:12px}
.newsletter h5{color:var(--white);font-size:12px;font-weight:700}
.field{left:680px;top:102px;width:290px;height:40px;background:var(--white)}
.field-btn{left:970px;top:102px;width:62px;height:40px;background:var(--purple);display:flex;align-items:center;justify-content:center}
.social{top:232px;width:34px;height:34px;border-radius:50%;background:var(--teal)}
.studio{left:832px;top:136px;color:#cfd3d9;font-size:11px;line-height:17px;width:220px}
.studio h5{color:var(--white);font-size:13px;margin-bottom:12px}
.studio .row{display:flex;gap:10px;margin-bottom:10px}
</style>
</head>
<body>

<section class="hero">
  <div class="media" role="img" aria-label="Man watching a screen in awe beside a bowl of popcorn" style="left:0;top:0;width:640px;height:633px;background:radial-gradient(ellipse at 30% 30%,#4e6a86 0%,#26303d 45%,rgba(14,17,23,0) 75%)"></div>
  <div class="media" role="img" aria-label="Tall black floor-standing speaker" style="left:700px;top:400px;width:340px;height:233px;background:linear-gradient(160deg,#3a3d44,#0f1115 70%)"></div>
  <div class="abs brand">BTD</div>
  <div class="abs search"><span>Search website</span>
    <svg width="12" height="12" viewBox="0 0 12 12"><circle cx="5" cy="5" r="3.8" fill="none" stroke="#9aa0aa" stroke-width="1.4"/><path d="M8 8l3 3" stroke="#9aa0aa" stroke-width="1.4"/></svg></div>
  <div class="abs call">CALL</div>
  <svg class="abs" style="left:1122px;top:44px" width="28" height="28" viewBox="0 0 28 28"><circle cx="12" cy="12" r="9" fill="none" stroke="#3cc7a5" stroke-width="2.5"/><path d="M19 19l7 7" stroke="#3cc7a5" stroke-width="2.5"/></svg>
  <div class="abs menu"></div>
  <h1 class="abs">More Affordable Than<br>You Might Think!</h1>
  <svg class="abs" style="left:1010px;top:312px" width="12" height="16" viewBox="0 0 12 16"><path d="M0 0l12 8-12 8z" fill="#c9e23a"/></svg>
  <p class="abs lead">Big screens, rich sound and a clean install. Front projection and full surround systems built for your room.</p>
</section>

<section class="what">
  <svg class="abs" style="left:560px;top:0" width="80" height="26" viewBox="0 0 80 26"><path d="M0 0h80L40 26z" fill="#23272f"/><path d="M34 10l6 6 6-6" stroke="#fff" stroke-width="1.5" fill="none"/></svg>
  <h2 class="abs">What we do...</h2>
  <p class="abs">We design and install home theaters for movies, sports and gaming on the big screen.</p>
  <div class="btn" style="left:160px;top:198px;width:112px">See More</div>
  <div class="media" role="img" aria-label="Floor-standing speaker tower" style="left:760px;top:0;width:440px;height:387px;background:linear-gradient(150deg,#6c4a8a 0%,#1a1b20 40%,#2c2d33 70%,#8d5cb6 100%)"></div>
  <div class="media" role="img" aria-label="Phone screen showing a messages app" style="left:525px;top:185px;width:230px;height:202px;background:linear-gradient(#9b5fd0 0 38px,#ffffff 38px);border-radius:8px 8px 0 0"></div>
</section>

<section class="features">
  <div class="feature" style="left:156px">
    <h3>Design &amp; Features</h3>
    <p class="sub">Clean layouts, hidden wiring and a screen sized right for every room.</p>
    <p class="body">We plan each room around the seats, light and sound so the picture and audio feel natural from every chair in the house.</p>
    <div class="btn">See More</div>
  </div>
  <div class="feature" style="left:450px">
    <h3>Pocket Power</h3>
    <p class="sub">Control the whole room from one simple remote or your phone.</p>
    <p class="body">Lights, screen, projector and sound all start with a single touch, so movie night begins the moment you sit down.</p>
    <div class="btn">Play More</div>
  </div>
  <div class="feature" style="left:742px">
    <h3>Inspired by the world</h3>
    <p class="sub">Ideas drawn from the best cinemas and studios we have seen.</p>
    <p class="body">We bring the look and feel of a real theater home, with gear chosen to match your space and your budget.</p>
    <div class="btn">Contact Us</div>
  </div>
  <svg class="abs" style="left:570px;top:368px" width="60" height="23" viewBox="0 0 60 23"><path d="M0 23L30 0l30 23z" fill="#23272f"/><rect x="26" y="6" width="8" height="14" rx="4" fill="none" stroke="#fff" stroke-width="1.3"/></svg>
</section>

<section class="who">
  <h2 class="abs">Who we are</h2>
  <p class="abs">A small team of installers who love film and sound. We build high end home theaters for families, fans and gamers, and we stay with you after the last cable is tidied away.</p>
  <div class="media" role="img" aria-label="Woman listening beside large speakers" style="left:228px;top:262px;width:712px;height:208px;background:linear-gradient(90deg,#cfc8c0 0%,#e9e6e2 35%,#2b2b2f 60%,#b7b3ae 100%)"></div>
  <div class="abs" style="left:502px;top:370px;width:150px;height:42px;border:2px solid #fff;color:#fff;font-size:16px;letter-spacing:3px;display:flex;align-items:center;justify-content:center">DONE</div>
</section>

<section class="values">
  <div class="value" style="left:156px">
    <svg width="36" height="30" viewBox="0 0 36 30"><rect x="2" y="2" width="32" height="22" fill="none" stroke="#3cc7a5" stroke-width="2"/><path d="M14 8l9 5-9 5z" fill="#3cc7a5"/><path d="M10 28h16" stroke="#3cc7a5" stroke-width="2"/></svg>
    <h4>Design</h4><p>Every room is drawn up with screen size, seat rows and speaker spots planned before any work starts.</p></div>
  <div class="value" style="left:375px">
    <svg width="40" height="30" viewBox="0 0 40 30"><rect x="2" y="6" width="26" height="20" fill="none" stroke="#3cc7a5" stroke-width="2"/><path d="M28 12l10-5v18l-10-5" fill="none" stroke="#3cc7a5" stroke-width="2"/></svg>
    <h4>Refinement</h4><p>We tune the picture and calibrate the sound until the room gives you a true cinema feeling.</p></div>
  <div class="value" style="left:594px">
    <svg width="36" height="30" viewBox="0 0 36 30"><path d="M3 10h7l9-7v24l-9-7H3z" fill="none" stroke="#3cc7a5" stroke-width="2"/><path d="M25 9q4 6 0 12M29 5q7 10 0 20" fill="none" stroke="#3cc7a5" stroke-width="2"/></svg>
    <h4>Dive In</h4><p>Sit down, press play and let full surround sound pull you into the game, match or film.</p></div>
  <div class="value" style="left:812px">
    <svg width="30" height="30" viewBox="0 0 30 30"><rect x="10" y="2" width="10" height="17" rx="5" fill="none" stroke="#3cc7a5" stroke-width="2"/><path d="M5 14q0 9 10 9t10-9M15 23v5" fill="none" stroke="#3cc7a5" stroke-width="2"/></svg>
    <h4>Research</h4><p>We test new projectors, screens and speakers so you get gear that is proven and built to last.</p></div>
  <div class="abs" style="left:558px;top:332px;width:50px;height:36px;background:#5a5e66;display:flex;align-items:center;justify-content:center">
    <svg width="14" height="16" viewBox="0 0 14 16"><path d="M0 0l14 8-14 8z" fill="#fff"/></svg></div>
</section>

<section class="gallery">
  <svg class="abs" style="left:156px;top:78px" width="24" height="20" viewBox="0 0 24 20"><path d="M6 18a5 5 0 010-10 7 7 0 0113-1 5 5 0 01-1 11z" fill="none" stroke="#6b7079" stroke-width="1.5"/></svg>
  <h2 class="abs">Gallery</h2>
  <p class="abs sub">A look at rooms we have built, from cozy dens to full dedicated theater spaces.</p>
  <p class="abs body">Browse our recent work to see screens, seats and speakers in real homes. Each project starts with a visit, a plan and a clear quote you can trust.</p>
  <div class="media" role="img" aria-label="Close view of black speaker towers" style="left:585px;top:0;width:615px;height:428px;background:linear-gradient(110deg,#d9dadd 0%,#2a2b30 35%,#8c8e94 55%,#1b1c20 75%,#cfd0d4 100%)"></div>
</section>

<section class="stories">
  <div class="media" role="img" aria-label="Hand holding a phone playing a video" style="left:148px;top:0;width:437px;height:342px;background:linear-gradient(135deg,#6d6f74,#2b2c30 60%,#4c4d52)"></div>
  <div class="abs quote-card">
    <div class="date">12 June 2019</div>
    <blockquote>Lorem ipsum dolor sit amet, cotur<br>adipiscing elit sed do eiusmod<br>tempor incididunt ut labore et dolore</blockquote>
    <div class="author"><span class="avatar"></span>Dan Holm</div>
  </div>
  <div class="abs tag">LATEST NEWS</div>
  <div class="abs post">
    <h3>Lorem ipsum dolor sit amet, consectetur<br>adipiscing elit</h3>
    <p>Short notes from our latest install, with tips on screen size, seating and sound for rooms of every shape.</p>
    <p style="margin-top:38px">92 &nbsp; Comments</p>
  </div>
  <div class="media" role="img" aria-label="Pair of speaker drivers in warm light" style="left:585px;top:342px;width:435px;height:228px;background:linear-gradient(90deg,#111 0%,#cfc9be 45%,#1a1a1c 70%,#3a3834 100%)"></div>
</section>

<section class="project">
  <div class="media" role="img" aria-label="Hand writing with a pen over printed sketches" style="left:0;top:0;width:1200px;height:570px;background:linear-gradient(160deg,#f3f2f0 0%,#b8b5b0 40%,#5e5a55 75%,#2d2b29 100%)"></div>
  <div class="abs panel">
    <h2>Your project</h2>
    <blockquote>Ut enim ad minim veniam,<br>quis nostrud exercitation<br>ullamco laboris. Nisi ut<br>aliquip ex ea commodo.</blockquote>
    <div class="author" style="color:#fff;margin-top:18px"><span class="avatar"></span>Dan Holm</div>
  </div>
</section>

<footer class="footer">
  <h2 class="abs">Contact Us</h2>
  <p class="abs intro"><strong style="color:#fff">Get in touch</strong><br>Tell us about your room, your budget and what you love to watch. We will reply within one working day with ideas and a time to visit your home.</p>
  <div class="links" style="left:156px"><h5>What we do</h5>Tour<br>Customers<br>Pricing and Plans<br>New Features<br>Education</div>
  <div class="links" style="left:306px"><h5>Who we are</h5>Tour<br>Customers<br>Pricing and Plans<br>New Features<br>Education</div>
  <div class="links" style="left:456px"><h5>Gallery</h5>Tour<br>Customers<br>Pricing and Plans<br>New Features<br>Education</div>
  <div class="abs newsletter" style="left:680px;top:76px"><h5>Stay in touch</h5></div>
  <div class="abs field"></div>
  <div class="abs field-btn"><svg width="18" height="14" viewBox="0 0 18 14"><path d="M1 7l5 5L17 1" fill="none" stroke="#fff" stroke-width="2"/></svg></div>
  <p class="abs" style="left:680px;top:150px;width:140px;color:#aeb3bb;font-size:10px;line-height:15px">Join our list for tips and offers. We never share your email.</p>
  <div class="abs social" style="left:684px"></div>
  <div class="abs social" style="left:726px"></div>
  <div class="abs social" style="left:768px"></div>
  <div class="abs studio">
    <h5>OUR STUDIO</h5>
    <div class="row"><svg width="12" height="16" viewBox="0 0 12 16"><path d="M6 15S1 9 1 6a5 5 0 0110 0c0 3-5 9-5 9z" fill="none" stroke="#cfd3d9" stroke-width="1.3"/><circle cx="6" cy="6" r="1.8" fill="#cfd3d9"/></svg><span>48 Lantern Row,<br>Dawnfield 20415</span></div>
    <div class="row"><svg width="14" height="14" viewBox="0 0 14 14"><path d="M3 1l3 3-2 2q2 3 4 4l2-2 3 3-2 2Q4 12 1 3z" fill="#cfd3d9"/></svg><span>(+00) 12-3456 7890</span></div>
  </div>
</footer>

</body>
</html>
```